Professional Services - letterhead / business cards

The company (velmora holdings) will provide services to Investment Funds and large investors in Spain. I have recently chosen a logo that I am attaching.

I would like a simple stationary design that i could use as letter head, business cards and "with compliments" cards.

I am not quite sure which color I will mostly use for the logo, in the email signature I will probably lean towards the white background and grey letters. I am attaching my favourite options.

Target Market(s)

Large Multinationals, Investment funds and Law firms

Industry/Entity Type

Business

Requirements
Must have
• my details are:
Luis R. Albarda
Velmora Holdings S.L.
Casa de Valdetorres
Calle de Ortuzar Beltrán 27
28019 Madrid
T: +34 (91) 387-6051
M: +34 (655) 814-073
e-mail: lalbarda@velmoraholdings.example

```html
<!DOCTYPE html>
<html lang="es">
<head>
<meta charset="utf-8">
<title>Velmora Holdings — Stationery</title>
<link rel="stylesheet" href="https://fonts.googleapis.com/css2?family=Questrial&display=swap">
<style>
  :root {
    --backdrop: #eeebe5;
    --paper: #ffffff;
    --navy-deep: #1b235f;
    --navy-light: #4a5290;
    --ink: #6a3a8c;
    --ink-soft: #8a7898;
    --on-navy: #f2f2f8;
  }
  * { box-sizing: border-box; margin: 0; padding: 0; }
  html, body { width: 1200px; height: 900px; overflow: hidden; }
  body {
    position: relative;
    background: var(--backdrop);
    font-family: "Questrial", "Century Gothic", sans-serif;
    color: var(--ink);
  }
  .sheet { position: absolute; background: var(--paper); }

  .wordmark { white-space: nowrap; letter-spacing: 0.2px; }

  /* Business card — front */
  .card-front {
    left: 47px; top: 52px; width: 234px; height: 115px;
    background: linear-gradient(200deg, var(--navy-light) 0%, var(--navy-deep) 45%, var(--navy-deep) 100%);
    color: var(--on-navy);
  }
  .card-front .wordmark { position: absolute; left: 49px; top: 44px; font-size: 15px; }
  .card-front .address-line {
    position: absolute; left: 0; right: 0; top: 99px;
    text-align: center; font-size: 6.6px;
  }

  /* Business card — back */
  .card-back { left: 304px; top: 52px; width: 233px; height: 115px; }
  .card-back .holder-name { position: absolute; left: 37px; top: 28px; font-size: 13px; }
  .contact-list { list-style: none; font-size: 7.5px; line-height: 12.5px; }
  .contact-list .key { display: inline-block; width: 20px; color: var(--ink-soft); }
  .card-back .contact-list { position: absolute; left: 38px; top: 60px; }

  /* Envelope / compliments */
  .envelope { left: 39px; top: 220px; width: 549px; height: 274px; }
  .envelope .wordmark { position: absolute; left: 36px; top: 44px; font-size: 17px; }
  .envelope .address-block { position: absolute; left: 37px; top: 85px; font-size: 8.2px; line-height: 13.3px; }
  .envelope .holder-name { position: absolute; left: 35px; top: 231px; font-size: 13px; }

  /* Letterhead */
  .letterhead { left: 622px; top: 38px; width: 518px; height: 734px; }
  .letterhead .wordmark { position: absolute; left: 37px; top: 52px; font-size: 17px; }
  .letterhead .address-block { position: absolute; left: 387px; top: 48px; font-size: 7.4px; line-height: 10px; }
  .letterhead .contact-list { position: absolute; left: 38px; top: 672px; font-size: 8px; line-height: 13px; }
</style>
</head>
<body>
  <section class="sheet card-front" aria-label="Business card front">
    <div class="wordmark">velmora holdings</div>
    <p class="address-line">Casa de Valdetorres Calle de Ortuzar Beltrán 27 28019 Madrid</p>
  </section>

  <section class="sheet card-back" aria-label="Business card back">
    <p class="holder-name">Luis R. Albarda</p>
    <ul class="contact-list">
      <li><span class="key">T</span>+34 (91) 387-6051</li>
      <li><span class="key">M</span>+34 (655) 814-073</li>
      <li><span class="key">E</span>lalbarda@velmoraholdings.example</li>
    </ul>
  </section>

  <section class="sheet envelope" aria-label="Compliments card">
    <div class="wordmark">velmora holdings</div>
    <address class="address-block" style="font-style:normal">
      Casa de Valdetorres<br>Calle de Ortuzar Beltrán 27<br>28019 Madrid
    </address>
    <p class="holder-name">Luis R. Albarda</p>
  </section>

  <section class="sheet letterhead" aria-label="Letterhead">
    <div class="wordmark">velmora holdings</div>
    <address class="address-block" style="font-style:normal">
      Casa de Valdetorres<br>Calle de Ortuzar Beltrán 27<br>28019 Madrid
    </address>
    <ul class="contact-list">
      <li><span class="key">T</span>+34 (91) 387-6051</li>
      <li><span class="key">M</span>+34 (655) 814-073</li>
      <li><span class="key">E</span>lalbarda@velmoraholdings.example</li>
    </ul>
  </section>
</body>
</html>
```